Flyer für Anbieter einer Fortbildung für Beratungslehrer
Zielgruppe
Wir bieten eine Fortbildung für Beratungslehrer an, welche mit immer komplexer werdenden psychischen Fällen arbeiten. Diese Fortbildung setzt sich gezielt mit der Stärkung des Selbstkonzepts, der Resilienz sowie dem Selbstwert auseinander. Wir stellen dabei die Anliegen der Klienten in den Fokus.
Das Angebot basiert auf dem Konzept des Lernfeld Zuversicht des Kurt- Wendland-Institut, Heidelberg
Aufgabenstellung
Die Inhalte der Fortbildung sollen enthalten sein.
Layout sollte unseren Arbeitsbereich im psychologischen Wohlbefinden widerspiegeln

```html
<!DOCTYPE html>
<html lang="de">
<head>
<meta charset="utf-8">
<title>Fortbildung für Beratungslehrer – Flyer</title>
<link href="https://fonts.googleapis.com/css2?family=Montserrat:wght@400;500;600;700&display=swap" rel="stylesheet">
<style>
  :root {
    --teal: #589c8d;
    --teal-text: #4f9585;
    --ink: #1e1e1e;
    --body: #2b2b2b;
    --muted: #555;
    --white: #ffffff;
    --frame: #222;
    --paper-grey: #f1f1f1;
  }
  * { box-sizing: border-box; margin: 0; padding: 0; }
  html, body { width: 900px; height: 1200px; overflow: hidden; background: var(--white); }
  body { position: relative; font-family: "Montserrat", sans-serif; color: var(--body); }

  .page {
    position: absolute; left: 109px; width: 683px; height: 482px;
    border: 1px solid var(--frame); overflow: hidden; background: var(--white);
  }
  .page--cover { top: 91px; }
  .page--inside { top: 628px; background: linear-gradient(115deg, #f6f6f6 0%, #ececec 35%, #f7f7f7 55%, #eeeeee 80%, #f8f8f8 100%); }
  .page-shapes { position: absolute; inset: 0; width: 100%; height: 100%; }

  .brand { position: absolute; display: flex; align-items: center; gap: 7px; }
  .brand-dot { width: 40px; height: 40px; border-radius: 50%; border: 2px solid currentColor; }
  .brand-name { font-size: 11px; font-weight: 500; letter-spacing: 1.5px; }
  .brand--light { left: 128px; top: 67px; color: var(--white); }
  .brand--dark { left: 395px; top: 62px; color: var(--teal-text); }

  .cover-title { position: absolute; left: 395px; top: 134px; color: var(--teal-text); font-size: 10.5px; font-weight: 700; line-height: 13.5px; }
  .cover-sub { position: absolute; left: 395px; top: 168px; color: var(--teal-text); font-size: 11px; font-weight: 600; }
  .cover-lead { position: absolute; left: 395px; top: 193px; color: var(--muted); font-size: 9.5px; line-height: 12px; }
  .cover-web { position: absolute; left: 126px; top: 427px; color: var(--ink); font-size: 9.5px; font-weight: 600; line-height: 11px; }

  .intro { position: absolute; left: 48px; top: 32px; width: 250px; color: var(--white); font-size: 9.5px; font-weight: 500; line-height: 10.4px; }
  .tab-label { position: absolute; left: 583px; top: 9px; color: var(--white); font-size: 9.5px; font-weight: 500; }

  .block { position: absolute; width: 252px; }
  .block h2 { color: var(--teal-text); font-size: 10.5px; font-weight: 700; line-height: 12.5px; margin-bottom: 9px; }
  .block p { font-size: 8.4px; line-height: 12.1px; text-align: justify; }
  .feature { margin-bottom: 6px; }
  .feature h3 { color: var(--teal-text); font-size: 8.4px; font-weight: 500; line-height: 12px; margin-bottom: 1px; }

  .block--inhalt { left: 48px; top: 132px; }
  .block--erwartet { left: 48px; top: 260px; }
  .block--warum { left: 383px; top: 132px; }
  .block--zielgruppe { left: 383px; top: 239px; }

  .cta { position: absolute; left: 414px; top: 397px; color: var(--white); font-size: 11px; font-weight: 600; line-height: 12.2px; }
</style>
</head>
<body>

<section class="page page--cover">
  <svg class="page-shapes" viewBox="0 0 1138 803" preserveAspectRatio="none" aria-hidden="false">
    <defs>
      <linearGradient id="forestStream" x1="0" y1="0" x2="0" y2="1">
        <stop offset="0" stop-color="#4f7a2a"/>
        <stop offset="0.35" stop-color="#8cc24a"/>
        <stop offset="0.6" stop-color="#6d6a3c"/>
        <stop offset="0.75" stop-color="#4fa79a"/>
        <stop offset="1" stop-color="#2f9a8f"/>
      </linearGradient>
    </defs>
    <rect class="cover-band" x="0" y="0" width="569" height="803" fill="var(--teal)"/>
    <polygon class="web-panel" points="182,687 569,687 569,803 144,803" fill="var(--white)"/>
    <polygon class="cover-photo" role="img" aria-label="Foto: Waldbach mit klarem türkisem Wasser zwischen grünen Bäumen" points="569,463 1138,511 1138,803 569,803" fill="url(#forestStream)"/>
  </svg>

  <div class="brand brand--light"><span class="brand-dot"></span><span class="brand-name">ZUVERSICHTSRAUM</span></div>
  <div class="brand brand--dark"><span class="brand-dot"></span><span class="brand-name">ZUVERSICHTSRAUM</span></div>

  <h1 class="cover-title">STÄRKUNG DES SELBSTKONZEPTS,<br>DES SELBSTWERTS UND DER RESILIENZ</h1>
  <p class="cover-sub">Fortbildung für Beratungslehrer</p>
  <p class="cover-lead">Stärkung des Selbstkonzepts,<br>des Selbstwerts und der Resilienz</p>
  <p class="cover-web">Mehr Informationen auf<br>www.zuversichtsraum.de</p>
</section>

<section class="page page--inside">
  <svg class="page-shapes" viewBox="0 0 1138 803" preserveAspectRatio="none">
    <rect class="intro-band" x="0" y="0" width="569" height="168" fill="var(--teal)"/>
    <polygon class="info-tab" points="946,0 1138,0 1138,54 929,54" fill="var(--teal)"/>
    <polygon class="cta-band" points="637,598 1138,598 1138,803 570,803" fill="var(--teal)"/>
  </svg>

  <p class="intro">Sie sind Beratungslehrer und möchten Ihre Klient*innen bestmöglich in ihrer persönlichen Entwicklung unterstützen? Dann ist diese Fortbildung genau das Richtige für Sie!</p>
  <span class="tab-label">Information</span>

  <div class="block block--inhalt">
    <h2>INHALT DER FORTBILDUNG</h2>
    <p>In dieser praxisorientierten Fortbildung lernen Sie, wie Sie Ihre Klient*innen gezielt in den Bereichen Selbstkonzept, Selbstwert und Resilienz stärken können. Basierend auf dem bewährten Konzept des Lernfelds Zuversicht werden Ihnen Methoden und Techniken vermittelt, die direkt in der Beratung anwendbar sind.</p>
  </div>

  <div class="block block--erwartet">
    <h2>WAS ERWARTET SIE?</h2>
    <div class="feature">
      <h3>1. Stärkung des Selbstkonzepts:</h3>
      <p>Erfahren Sie, wie Sie Klient*innen helfen können, ein gesundes und positives Selbstbild zu entwickeln.</p>
    </div>
    <div class="feature">
      <h3>2. Aufbau von Selbstwert:</h3>
      <p>Entdecken Sie Wege, um das Selbstvertrauen und die Eigenmotivation Ihrer Klient*innen nachhaltig zu fördern.</p>
    </div>
    <div class="feature">
      <h3>3. Förderung der Resilienz</h3>
      <p>Lernen Sie Strategien kennen, mit denen Klient*innen Krisen und Herausforderungen besser bewältigen können.</p>
    </div>
  </div>

  <div class="block block--warum">
    <h2>WARUM DAS LERNFELD ZUVERSICHT?</h2>
    <p>Das Lernfeld Zuversicht verbindet positive Psychologie mit pädagogischen Ansätzen und ermöglicht eine ganzheitliche Förderung der Persönlichkeit. Ziel ist es, Klient*innen auf ein erfülltes und zufriedenes Leben vorzubereiten.</p>
  </div>

  <div class="block block--zielgruppe">
    <h2>FÜR WEN IST DIE<br>FORTBILDUNG GEEIGNET?</h2>
    <p>Diese Fortbildung richtet sich an Beratungslehrer, Schulpsychologen und pädagogische Fachkräfte, die ihre Kompetenzen erweitern und ihre Klient*innen bestmöglich unterstützen möchten.</p>
  </div>

  <p class="cta">Investieren Sie in die Zukunft<br>Ihrer Klient*innen – und in<br>Ihre eigene Weiterbildung!</p>
</section>

</body>
</html>
```